Business Card - Tally Forge

Need Business Card design for company named Tally Forge. Software development focused mainly on Brindle Kelvox & Vuro Apps. I've attached our logo with both a black and white background. Please add trademark symbol to logo when using.

```html
<!DOCTYPE html>
<html lang="en">
<head>
<meta charset="utf-8">
<title>Tally Forge — Business Card</title>
<link rel="stylesheet" href="https://fonts.googleapis.com/css2?family=Ubuntu:wght@500&family=Open+Sans:wght@400&display=swap">
<style>
  :root {
    --backdrop: #2a2a2a;
    --card: #ffffff;
    --ink: #333333;
    --charcoal: #353535;
    --red: #d8202a;
    --orange: #e8892a;
    --yellow: #f6bd22;
  }
  * { box-sizing: border-box; margin: 0; padding: 0; }
  html, body { width: 1200px; height: 1000px; overflow: hidden; }
  body {
    background: var(--backdrop);
    display: flex;
    flex-direction: column;
    align-items: center;
    justify-content: center;
    gap: 44px;
  }
  .card {
    position: relative;
    width: 760px;
    height: 434px;
    background: var(--card);
    box-shadow: 0 10px 30px rgba(0,0,0,0.45);
    overflow: hidden;
  }
  .band {
    position: absolute;
    left: 0; right: 0;
    height: 22px;
    display: flex;
  }
  .band--top { top: 0; }
  .band--bottom { bottom: 0; }
  .band span { display: block; height: 100%; }
  .band .seg-dark { background: var(--charcoal); }
  .band .seg-red { background: var(--red); }
  .band .seg-orange { background: var(--orange); }
  .band .seg-yellow { background: var(--yellow); }

  .brand {
    display: flex;
    align-items: center;
    gap: 16px;
    font-family: "Ubuntu", sans-serif;
    font-weight: 500;
    color: var(--ink);
    letter-spacing: -0.5px;
  }
  .brand-dot {
    border-radius: 50%;
    background: var(--orange);
    flex: none;
  }
  .card--front .brand {
    position: absolute;
    left: 50%; top: 50%;
    transform: translate(-50%, -50%);
    font-size: 58px;
  }
  .card--front .brand-dot { width: 40px; height: 40px; }

  .card--back .brand {
    position: absolute;
    left: 60px; top: 188px;
    font-size: 40px;
  }
  .card--back .brand-dot { width: 30px; height: 30px; }

  .contact-list {
    position: absolute;
    left: 390px; top: 110px;
    list-style: none;
    display: flex;
    flex-direction: column;
    gap: 26px;
    font-family: "Open Sans", sans-serif;
    font-size: 19px;
    color: var(--ink);
  }
  .contact-item { display: flex; align-items: center; gap: 16px; }
  .contact-icon {
    width: 34px; height: 34px;
    border-radius: 50%;
    display: flex; align-items: center; justify-content: center;
    flex: none;
  }
  .contact-icon--phone { background: var(--yellow); }
  .contact-icon--mail { background: var(--orange); }
  .contact-icon--pin { background: var(--red); }
  .contact-icon svg { width: 18px; height: 18px; }
</style>
</head>
<body>

  <section class="card card--front" aria-label="Card front">
    <div class="band band--top">
      <span class="seg-dark" style="width:22%"></span>
      <span class="seg-red" style="width:20%"></span>
      <span class="seg-orange" style="width:20%"></span>
      <span class="seg-yellow" style="width:22%"></span>
      <span class="seg-dark" style="width:16%"></span>
    </div>
    <div class="brand">
      <span class="brand-dot"></span>
      <span class="brand-name">Tally Forge</span>
    </div>
    <div class="band band--bottom">
      <span class="seg-dark" style="width:22%"></span>
      <span class="seg-red" style="width:20%"></span>
      <span class="seg-orange" style="width:20%"></span>
      <span class="seg-yellow" style="width:22%"></span>
      <span class="seg-dark" style="width:16%"></span>
    </div>
  </section>

  <section class="card card--back" aria-label="Card back">
    <div class="brand">
      <span class="brand-dot"></span>
      <span class="brand-name">Tally Forge</span>
    </div>
    <ul class="contact-list">
      <li class="contact-item">
        <span class="contact-icon contact-icon--phone">
          <svg viewBox="0 0 18 18"><rect x="5" y="1.5" width="8" height="15" rx="1.5" fill="none" stroke="#fff" stroke-width="1.6"/><circle cx="9" cy="14" r="0.9" fill="#fff"/></svg>
        </span>
        <span>555-014-2280</span>
      </li>
      <li class="contact-item">
        <span class="contact-icon contact-icon--mail">
          <svg viewBox="0 0 18 18"><rect x="2" y="4" width="14" height="10" rx="1" fill="#fff"/><path d="M2.5 4.5 L9 10 L15.5 4.5" fill="none" stroke="#e8892a" stroke-width="1.3"/></svg>
        </span>
        <span>555-017-6431</span>
      </li>
      <li class="contact-item">
        <span class="contact-icon contact-icon--pin">
          <svg viewBox="0 0 18 18"><path d="M9 16.5 C5 11.5 4 9.5 4 7 a5 5 0 0 1 10 0 c0 2.5-1 4.5-5 9.5z" fill="#fff"/><circle cx="9" cy="7" r="1.8" fill="#d8202a"/></svg>
        </span>
        <span>2140 Harbor Row, Fairhaven, FL 34020</span>
      </li>
    </ul>
    <div class="band band--bottom">
      <span class="seg-dark" style="width:22%"></span>
      <span class="seg-red" style="width:20%"></span>
      <span class="seg-orange" style="width:20%"></span>
      <span class="seg-yellow" style="width:22%"></span>
      <span class="seg-dark" style="width:16%"></span>
    </div>
  </section>

</body>
</html>
```